Copper Finch Agency Website - Wordpress Web UPDATED BRIEF

FINAL LOGO UPLOADED - please look to this as reference for how we would like the site to look and feel.

We are a digital marketing agency - looking to have a new website built. We are looking for a simple one page feel of site that will allow us to grow it later. (Feel free to take some liberties with that if your imagination veers off) Must be very, playful, bold, sleek and easily integrate video. Wordpress only.

Overview:

Copper Finch is a creative constellation. We are built on what's great about the shared economy. With access to thousands of content creators, designers, technicians, writers, strategists and other creatives around the world, we are built differently than a traditional “brick and mortar” Marketing Agency. We provide the traditional services our clients have come to expect, without the “5X factor” of covering the overhead common in the old agency model. We believe even better work can be created in collaboration with our clients and by passing those savings back to them for their use. Our clients pay for our art, our work and our passion –not our furniture.

"Copper Finch, Let's Start Something"

Target Market(s)

companies looking for creative agency help, video production, creative consulting and coaching

Industry/Entity Type

Digital Marketing

Coding

Coded - Design and coding required

Number of Pages Required

1 page

Font styles to use
Sans Serif

Colors
3277b5
33a6d7
ec1f27

Requirements
Must have
• Wordpress design is a must. Looking for a one sheet homepage - with sections that are all on the main front page. We will have videos to embed, and should be able to have client logos and easy access to show a variety of our creative work.
• Please look to the logo for how we would like the site to feel.
• Please think "icon process flow" instead of blocks of text (which we used to have). Use the text to explain what the process flow should represent - don't actually copy paste the text but show it visually in icons.
Nice to have
• innovation around how we show video content. solid colors complementary to our palette and aesthetic.
Should not have
• Standard HTML coding

```html
<!DOCTYPE html>
<html lang="en">
<head>
<meta charset="utf-8">
<title>Copper Finch Agency</title>
<link href="https://fonts.googleapis.com/css2?family=Rubik:wght@400;500;700&display=swap" rel="stylesheet">
<style>
:root{
  --blue:#3277b5;
  --sky:#33a6d7;
  --red:#ec1f27;
  --navy:#1d4f86;
  --footer:#2c5f9e;
  --white:#ffffff;
  --soft:rgba(255,255,255,.78);
  --line:rgba(255,255,255,.35);
}
*{box-sizing:border-box;margin:0;padding:0}
html,body{width:1200px;height:4091px;overflow:hidden}
body{position:relative;font-family:"Rubik",sans-serif;color:var(--white);
  background:linear-gradient(180deg,#2f84cc 0%,#3a92d6 18%,#3587cc 40%,#3a8fd3 55%,#2f78bb 68%,#3681c3 80%,#5a9bd3 93%,#7fb2dd 100%)}
.abs{position:absolute}
.waves{position:absolute;left:0;top:0;width:1200px;height:4091px}
/* header */
.brand{left:82px;top:40px;display:flex;align-items:center;gap:14px;font-weight:700;font-size:26px;letter-spacing:.5px}
.brand-dot{width:58px;height:58px;border-radius:50%;background:var(--white)}
.nav{left:477px;top:58px;display:flex;gap:28px;font-size:13px;font-weight:500}
.btn-red{background:var(--red);color:var(--white);border-radius:30px;font-weight:500;text-align:center}
.nav-cta{left:1015px;top:46px;width:98px;height:42px;line-height:42px;font-size:13px}
.btn-ghost{border:2px solid var(--white);border-radius:30px;color:var(--white);font-size:13px;font-weight:500;text-align:center}
/* hero */
.hero-title{left:87px;top:252px;font-size:38px;font-weight:700;line-height:48px;width:340px}
.hero-sub{left:87px;top:415px;width:240px;font-size:13px;line-height:21px;color:var(--soft)}
.hero-cta{left:87px;top:491px;width:115px;height:38px;line-height:34px}
.hero-art{left:464px;top:82px;width:654px;height:654px;border-radius:50%;
  background:radial-gradient(circle at 55% 45%,rgba(255,214,80,.35),rgba(60,150,220,.4) 45%,rgba(40,120,200,0) 72%)}
/* cards */
.card{background:var(--white);border-radius:10px;color:#2b3a4d;text-align:center;padding:38px 24px 0;box-shadow:0 14px 30px rgba(10,50,100,.25)}
.card svg{display:block;margin:0 auto 18px}
.card h3{font-size:17px;font-weight:500;margin-bottom:12px}
.card p{font-size:12px;line-height:19px;color:#6c7787}
.card a{display:block;margin-top:22px;font-size:11px;color:var(--blue);text-decoration:none}
/* about */
.character{left:109px;top:982px;width:436px;height:573px;border-radius:48% 48% 40% 40%;
  background:radial-gradient(ellipse at 50% 40%,rgba(230,90,60,.35),rgba(60,150,220,.35) 55%,rgba(50,130,210,0) 75%)}
.about-title{left:633px;top:1172px;font-size:33px;font-weight:500;line-height:44px;width:500px}
.about-text{left:633px;top:1285px;width:470px;font-size:12px;line-height:21px;color:var(--soft)}
.about-cta{left:633px;top:1407px;width:110px;height:38px;line-height:34px}
/* services */
.section-title{left:0;width:1200px;text-align:center;font-weight:500}
.service{display:flex;gap:26px;width:510px}
.service-icon{width:115px;height:115px;border-radius:50%;background:var(--white);flex:none;display:flex;align-items:center;justify-content:center}
.service h4{font-size:16px;font-weight:500;margin:6px 0 6px}
.service p{font-size:12px;line-height:19px;color:var(--soft)}
.rule-v{left:600px;width:1px;background:var(--line)}
.rule-h{height:1px;background:var(--line)}
.arrow{font-size:22px;color:var(--soft)}
.explore-cta{left:535px;top:1991px;width:128px;height:38px;line-height:34px}
/* work */
.slide{top:2323px;height:360px;border-radius:4px}
.slide-main{left:207px;width:786px;background:linear-gradient(135deg,#2bb2c4,#1f7fa8 55%,#15466f)}
.slide-left{left:0;width:147px;background:linear-gradient(90deg,#f4f6f8,#f7c531)}
.slide-right{left:1053px;width:147px;background:linear-gradient(90deg,#17324f,#e94a5a)}
.caption{left:256px;top:2602px}
.caption b{display:block;font-size:19px;font-weight:500}
.caption span{font-size:13px}
.dots{left:545px;top:2754px;display:flex;gap:14px}
.dots i{width:14px;height:14px;border-radius:50%;border:2px solid var(--white);display:block}
.dots i:first-child{background:var(--white)}
/* testimonials */
.avatar{width:110px;height:110px;border-radius:50%;background:linear-gradient(135deg,#d8b49a,#7a5a46);border:4px solid var(--white)}
.quote{width:360px;font-size:16px;line-height:25px}
.who{font-size:12px;line-height:18px}
.who b{font-weight:500}
/* clients */
.clients-line{top:3374px;height:1px;background:var(--line)}
.client{top:3462px;width:180px;text-align:center;font-size:20px;font-weight:700;color:var(--soft)}
/* form */
.field{background:var(--white);border-radius:12px;color:#9aa3ae;font-size:12px;padding:0 18px;line-height:39px;height:39px}
.field.tall{height:93px;line-height:1;padding-top:13px}
.submit{left:545px;top:3908px;width:110px;height:38px;line-height:38px;font-size:13px}
/* footer */
.footer{left:0;top:4031px;width:1200px;height:60px;background:var(--footer);font-size:11px;color:var(--soft)}
.footer span{position:absolute;top:22px;letter-spacing:.5px}
.social{position:absolute;top:0;height:60px;display:flex;align-items:center;justify-content:center;font-size:12px;color:var(--white)}
</style>
</head>
<body>

<svg class="waves" viewBox="0 0 1200 4091" aria-hidden="true">
  <path d="M0 0H1200V620C1000 760 760 880 560 900C360 920 160 880 0 960Z" fill="rgba(255,255,255,.05)"/>
  <path d="M0 1560C300 1480 800 1480 1200 1580V2100C900 2250 400 2350 0 2300Z" fill="rgba(20,70,140,.12)"/>
  <path d="M0 2050C300 2160 700 2120 1200 1980V2120C800 2300 300 2300 0 2200Z" fill="rgba(255,255,255,.07)"/>
  <path d="M0 2800C400 2700 900 2900 1200 2780V2900C800 3000 400 2850 0 2930Z" fill="rgba(255,255,255,.05)"/>
  <path d="M0 3920L180 3870L360 3930L560 3860L760 3940L960 3880L1200 3930V4031H0Z" fill="rgba(255,255,255,.12)"/>
</svg>

<header>
  <div class="abs brand"><span class="brand-dot"></span>Copper Finch</div>
  <nav class="abs nav">
    <span>Home</span><span>About</span><span>Service</span><span>Work</span><span>Client</span><span>Reviews</span><span>Call. 555.014.2290</span>
  </nav>
  <div class="abs btn-red nav-cta">Contact</div>
</header>

<section class="hero">
  <div class="abs hero-art" role="img" aria-label="Illustration of a marketing team around a megaphone, video screen and social icons"></div>
  <h1 class="abs hero-title">Leading Best Digital Marketing Agency.</h1>
  <p class="abs hero-sub">We are a digital marketing agency new website built.</p>
  <div class="abs btn-ghost hero-cta">Contact Us</div>

  <div class="abs card" style="left:207px;top:641px;width:240px;height:204px">
    <svg width="40" height="40" viewBox="0 0 40 40" fill="none" stroke="#1d4f86" stroke-width="2"><circle cx="17" cy="17" r="10"/><path d="M25 25l9 9"/></svg>
    <h3>Discovery.</h3><p>We are passionate about creating with you, not just for you.</p><a>Learn More →</a>
  </div>
  <div class="abs card" style="left:480px;top:704px;width:240px;height:278px;padding-top:48px">
    <svg width="40" height="40" viewBox="0 0 40 40" fill="none" stroke="#1d4f86" stroke-width="2"><path d="M10 6v30M10 8h20l-5 7 5 7H10"/></svg>
    <h3>Strategy.</h3><p>Content is only as good as your plan to deliver it.</p><a>Learn More →</a>
  </div>
  <div class="abs card" style="left:753px;top:785px;width:240px;height:279px;padding-top:48px">
    <svg width="40" height="40" viewBox="0 0 40 40" fill="none" stroke="#1d4f86" stroke-width="2"><path d="M20 4l10 14-10 18L10 18z"/><circle cx="20" cy="20" r="3"/></svg>
    <h3>Creative.</h3><p>We are ready for our close up! Are you?</p><a>Learn More →</a>
  </div>
</section>

<section class="about">
  <div class="abs character" role="img" aria-label="Illustrated mascot in a cap holding a lit match"></div>
  <h2 class="abs about-title">Copper Finch is a Creative Constellation.</h2>
  <p class="abs about-text">We are built on what's great about the shared economy. With access to thousands of content creators, designers, technicians, writers, strategists and other creatives around the world, we are built differently than a traditional "brick and mortar" Marketing Agency.</p>
  <div class="abs btn-ghost about-cta">About Us</div>
</section>

<section class="services">
  <h2 class="abs section-title" style="top:1560px;font-size:27px">Service We offer</h2>
  <div class="abs arrow" style="left:30px;top:1770px">‹</div>
  <div class="abs arrow" style="left:1150px;top:1770px">›</div>
  <div class="abs rule-v" style="top:1640px;height:120px"></div>
  <div class="abs rule-v" style="top:1812px;height:140px"></div>
  <div class="abs rule-h" style="left:90px;top:1786px;width:480px"></div>
  <div class="abs rule-h" style="left:633px;top:1786px;width:480px"></div>

  <div class="abs service" style="left:90px;top:1636px">
    <div class="service-icon"><svg width="46" height="46" viewBox="0 0 46 46" fill="none" stroke="#1d4f86" stroke-width="2.5"><circle cx="23" cy="15" r="8"/><path d="M8 40c2-10 8-14 15-14s13 4 15 14"/></svg></div>
    <div><h4>Management</h4><p>At vero eos et accusamus et iusto odio dignissimos ducimus qui blanditiis praesentium voluptatum deleniti atque corrupti quos dolores ...</p></div>
  </div>
  <div class="abs service" style="left:635px;top:1636px">
    <div class="service-icon"><svg width="46" height="46" viewBox="0 0 46 46" fill="none" stroke="#1d4f86" stroke-width="2.5"><path d="M12 6h16l8 8v26H12z"/><path d="M17 20h14M17 26h14M17 32h10"/></svg></div>
    <div><h4>Content</h4><p>At vero eos et accusamus et iusto odio dignissimos ducimus qui blanditiis praesentium voluptatum deleniti atque corrupti quos dolores ...</p></div>
  </div>
  <div class="abs service" style="left:90px;top:1827px">
    <div class="service-icon"><svg width="46" height="46" viewBox="0 0 46 46" fill="none" stroke="#1d4f86" stroke-width="2.5"><path d="M8 18h8l16-9v28l-16-9H8z"/><path d="M13 28l3 10h5l-2-10"/></svg></div>
    <div><h4>Production</h4><p>At vero eos et accusamus et iusto odio dignissimos ducimus qui blanditiis praesentium voluptatum deleniti atque corrupti quos dolores ...</p></div>
  </div>
  <div class="abs service" style="left:635px;top:1827px">
    <div class="service-icon"><svg width="46" height="46" viewBox="0 0 46 46" fill="none" stroke="#1d4f86" stroke-width="2.5"><circle cx="23" cy="23" r="17"/><path d="M28 16c-2-2-9-2-9 2s10 3 10 8-8 5-11 2M23 11v24"/></svg></div>
    <div><h4>Paid Media</h4><p>At vero eos et accusamus et iusto odio dignissimos ducimus qui blanditiis praesentium voluptatum deleniti atque corrupti quos dolores ...</p></div>
  </div>
  <div class="abs btn-ghost explore-cta">Explore All</div>
</section>

<section class="work">
  <h2 class="abs section-title" style="top:2218px;font-size:38px">Explore Our Work</h2>
  <div class="abs slide slide-left" role="img" aria-label="Project preview of a web dashboard"></div>
  <div class="abs slide slide-main" role="img" aria-label="Project preview of a data management web application on a laptop"></div>
  <div class="abs slide slide-right" role="img" aria-label="Project preview of a web interface"></div>
  <div class="abs caption"><b>Big Data Management System Frontend</b><span>Web Application</span></div>
  <div class="abs dots"><i></i><i></i><i></i><i></i><i></i></div>
</section>

<section class="reviews">
  <h2 class="abs section-title" style="top:2968px;font-size:35px">What Our Clients Say</h2>
  <div class="abs arrow" style="left:30px;top:3128px">‹</div>
  <div class="abs arrow" style="left:1150px;top:3128px">›</div>
  <div class="abs avatar" style="left:95px;top:3068px" role="img" aria-label="Portrait photo of client Dana Whitlow"></div>
  <p class="abs quote" style="left:240px;top:3070px">"There are many variations of passages of Lorem Ipsum available, but the majority have suffered alteration in some form, by injected humour, or randomised words which don't look even slightly believable."</p>
  <p class="abs who" style="left:240px;top:3246px"><b>Dana Whitlow,</b><br>Harbor Stage</p>
  <div class="abs avatar" style="left:633px;top:3068px;background:linear-gradient(135deg,#c9a58a,#5b4436)" role="img" aria-label="Portrait photo of client Milo Brandt"></div>
  <p class="abs quote" style="left:783px;top:3070px">"There are many variations of passages of Lorem Ipsum available, but the majority have suffered alteration in some form, by injected humour, or randomised words which don't look even slightly believable."</p>
  <p class="abs who" style="left:783px;top:3246px"><b>Milo Brandt</b><br>Collective</p>
</section>

<section class="clients">
  <div class="abs clients-line" style="left:87px;width:430px"></div>
  <h2 class="abs section-title" style="top:3356px;font-size:27px">Clients</h2>
  <div class="abs clients-line" style="left:683px;width:430px"></div>
  <div class="abs client" style="left:95px">Northway</div>
  <div class="abs client" style="left:300px">Brightmill</div>
  <div class="abs client" style="left:510px">Halvane</div>
  <div class="abs client" style="left:717px">Brightmill</div>
  <div class="abs client" style="left:925px">Northway</div>
</section>

<section class="contact">
  <h2 class="abs section-title" style="top:3606px;font-size:35px;line-height:42px">Copper Finch, Let's Start<br>Something!</h2>
  <div class="abs field" style="left:207px;top:3722px;width:385px">Enter your name*</div>
  <div class="abs field" style="left:207px;top:3780px;width:385px">E-mail*</div>
  <div class="abs field" style="left:207px;top:3834px;width:385px">Phone</div>
  <div class="abs field" style="left:608px;top:3722px;width:385px">Project Type*</div>
  <div class="abs field tall" style="left:608px;top:3780px;width:385px">Message</div>
  <div class="abs btn-red submit">Submit</div>
</section>

<footer class="abs footer">
  <span style="left:82px">© 2018 COPPER FINCH</span>
  <span style="left:245px">P. 555.014.2290</span>
  <span style="left:360px">E. CONTACT@COPPERFINCH.CO</span>
  <div class="social" style="left:976px;width:60px">
    <svg width="16" height="22" viewBox="0 0 16 22" fill="none" stroke="#fff" stroke-width="2"><path d="M8 21s7-8 7-13A7 7 0 0 0 1 8c0 5 7 13 7 13z"/><circle cx="8" cy="8" r="2.5"/></svg>
  </div>
  <div class="social" style="left:1050px;width:68px;background:#24528a">Orvix</div>
  <div class="social" style="left:1118px;width:82px;background:#3a6fae">Qelto</div>
</footer>

</body>
</html>
```